Retro Label for old fashioned soda

We need a label for soda we are having private labeled for our retro, 1950's ice cream shop www.thefrostyparlor.net I don't want the label to look like something from 2017 with a retro feel, but more like an original (possibly kinda cheesy) label you'd see from the 1950's with some of the old catch lines like "tastes great", "invigorating" or "it is refreshing!" The prominent brand should be the name of our ice cream shop, The Frosty Parlor. the soda is also pure cane sugar so it might be good to have that on somewhere

Label size is 2.4" wide by 4" tall. Here is an example of some retro labels from lookfindr. I attached on file to this contest but there are more here: https://www.lookfindr.net/results?q=retro+soda+label&id=8Hq2Lm4Pz7Vb1Kc9Xw3Rt6Yd0Ns5Jf2Ga8Ue4Ko1Mi7Bl3Wp9Dv6Qx2Hc5Zr0Ty8Fn4#img=Pk7Rw2Lx9Qm3:

The label will be the same for all the flavors with the exception of the flavor name changing somewhere on the label. These are the flavors

Root Beer
Orange
Black Cherry
Lemonade
Raspberry Lime -Rickey
White Birch Beer
Lemon Iced Tea
Vanilla Cream
Orange Cream
Sarsaparilla
Ginger Ale

• retro feel. authentic old fashioned look

```html
<!DOCTYPE html>
<html lang="en">
<head>
<meta charset="utf-8">
<title>The Frosty Parlor – White Birch Beer Label</title>
<link rel="stylesheet" href="https://fonts.googleapis.com/css2?family=Arvo:wght@400;700&family=Varela+Round&family=Lobster&family=Lora:wght@600&display=swap">
<style>
  :root {
    --teal: #76b8b3;
    --coral: #f56a6c;
    --cream: #f2e3d3;
    --ink: #111111;
    --white: #ffffff;
    --backdrop: #ffffff;
  }
  html, body {
    margin: 0;
    padding: 0;
    width: 1200px;
    height: 1200px;
    overflow: hidden;
    background: var(--backdrop);
  }
  .canvas {
    position: relative;
    width: 1200px;
    height: 1200px;
  }
  .soda-label {
    position: absolute;
    left: 251px;
    top: 42px;
    width: 698px;
    height: 1116px;
    box-shadow: 22px 26px 28px rgba(0, 0, 0, 0.22);
  }
  .soda-label svg { display: block; width: 100%; height: 100%; }
  .label-ground { fill: var(--teal); }
  .band-cream { fill: var(--cream); }
  .band-coral { fill: var(--coral); }
  .slogan {
    font-family: "Arvo", serif;
    fill: var(--coral);
  }
  .tagline {
    font-family: "Varela Round", sans-serif;
    fill: var(--white);
    font-size: 44px;
    letter-spacing: 1px;
  }
  .brand-name {
    font-family: "Lobster", cursive;
    fill: var(--ink);
    font-size: 88px;
    word-spacing: 16px;
  }
  .flavor-name {
    font-family: "Lora", serif;
    font-weight: 600;
    fill: var(--white);
    font-size: 47px;
    letter-spacing: 1px;
  }
</style>
</head>
<body>
<main class="canvas">
  <div class="soda-label">
    <svg viewBox="0 0 665 1063" xmlns="http://www.w3.org/2000/svg">
      <defs>
        <clipPath id="label-edge"><rect width="665" height="1063"/></clipPath>
      </defs>
      <g clip-path="url(#label-edge)">
        <rect class="label-ground" width="665" height="1063"/>

        <g class="slogan-stack slogan-top">
          <text class="slogan" x="35" y="87" font-size="81">it tastes great!</text>
          <text class="slogan" x="35" y="147" font-size="66">it tastes great!</text>
          <text class="slogan" x="37" y="200" font-size="52">it tastes great!</text>
          <text class="slogan" x="39" y="243" font-size="38">it tastes great!</text>
        </g>

        <g class="diagonal-bands" transform="translate(0,558) rotate(-24.6)">
          <rect class="band-cream" x="-400" y="0" width="1400" height="247"/>
          <rect class="band-coral" x="-400" y="-86" width="996" height="86"/>
          <rect class="band-coral" x="8" y="247" width="1000" height="86"/>

          <text class="tagline" x="56" y="-26">pure cane sugar soda</text>
          <text class="brand-name" x="310" y="158" text-anchor="middle">The Frosty Parlor</text>
          <text class="flavor-name" x="135" y="306">White Birch Beer</text>
        </g>

        <g class="slogan-stack slogan-bottom" text-anchor="end">
          <text class="slogan" x="632" y="843" font-size="38">it tastes great!</text>
          <text class="slogan" x="632" y="887" font-size="52">it tastes great!</text>
          <text class="slogan" x="633" y="947" font-size="66">it tastes great!</text>
          <text class="slogan" x="635" y="1008" font-size="81">it tastes great!</text>
        </g>
      </g>
    </svg>
  </div>
</main>
</body>
</html>
```